Granite Tile Retail Website

We need wireframe PSD for a website selling granite tile. There are 4 custom pages, shopping cart page, and checkout page. I have a logo designed but the color scheme is up to you.
Color Gallery - We have approximately 20 different stone colors. Each color will have a little gallery of its own pictures. On this page the customer can also add a sample piece of the color they are viewing to their shopping cart.
Questions Page - This page has 3 elements
1. Upload or fax diagram of kitchen for quotation
2. Installation video
3. Installation FAQ (text)
Order Page - This page has 3 steps for the customer
1. Customer chooses his color.
2. For each color we have numerous different products. He inputs the quantity of each product.
3. Customer is given total price and shipping quote. If order over $500 it says "This order qualifies for free shipping". Customer can click on button to "Order Now"
Shopping Cart - Very standard, just like I have attached here. Just modify for your colors / font.
Checkout - Just like in the attached. See design-explanation.docx for minor adjustments.
I have vector file for logo.
Please try to post your designs by tonightÂ
Home owners 40-60 years old
Shopping

```html
<!DOCTYPE html>
<html lang="en">
<head>
<meta charset="utf-8">
<title>Checkout – Stoneleaf Granite</title>
<link href="https://fonts.googleapis.com/css2?family=Oswald:wght@500;600&family=Mulish:wght@400;600;700&display=swap" rel="stylesheet">
<style>
:root{
  --page:#efefef;
  --frame:#ffffff;
  --ink:#3b3b3b;
  --muted:#555;
  --rule:#d8d8d8;
  --field:#fafafa;
  --field-line:#c9c9c9;
  --maroon:#6b1a2c;
  --gold:#f0ad34;
  --gold-dark:#d8922a;
  --banner-dark:#2b2824;
  --banner-mid:#4a4540;
  --band:#f3f3f3;
}
*{box-sizing:border-box;margin:0;padding:0}
html,body{width:1029px;height:1200px;overflow:hidden;background:var(--page)}
body{font-family:"Mulish",sans-serif;color:var(--ink);font-size:15px;letter-spacing:.3px}
.canvas{position:relative;width:1029px;height:1200px}
.frame{position:absolute;left:38px;top:38px;width:953px;height:1134px;background:var(--frame);border:1px solid #e2e2e2}
.abs{position:absolute}

/* header */
.site-header{left:57px;top:62px;width:915px;height:114px;border-top:1px solid #e4e4e4;border-bottom:1px solid #dcdcdc;background:linear-gradient(#ffffff,#efefef)}
.brand{left:86px;top:96px;display:flex;align-items:center;gap:10px}
.brand-mark{width:26px;height:26px;background:var(--gold)}
.brand-name{font-family:"Oswald",sans-serif;font-weight:600;font-size:30px;color:var(--maroon);letter-spacing:1px}
.main-nav{left:520px;top:92px;height:56px;display:flex;align-items:center}
.main-nav a{font-family:"Oswald",sans-serif;font-weight:500;font-size:20px;color:#3a3a3a;text-decoration:none;padding:0 10px;height:56px;line-height:56px;border-right:1px solid #9a9a9a;letter-spacing:-.2px}
.main-nav a:last-child{border-right:none}
.main-nav a.current{color:var(--gold)}

.page-title{left:67px;top:216px;font-family:"Oswald",sans-serif;font-weight:500;font-size:26px;color:#333;letter-spacing:-.5px}

/* section banners */
.banner{width:241px;height:58px}
.banner svg{position:absolute;left:0;top:0}
.banner span{position:absolute;left:0;top:0;width:241px;height:48px;display:flex;align-items:center;justify-content:center;gap:10px;font-family:"Oswald",sans-serif;font-weight:500;font-size:24px;color:var(--gold);letter-spacing:-.3px}
.divider{width:1px;background:var(--rule);top:257px;height:648px}

.label{font-size:15px;color:var(--ink);white-space:nowrap}
.label sup{color:#b23;font-size:11px;margin-left:2px}
.field{height:29px;background:var(--field);border:1px solid var(--field-line)}
.select{height:31px;border:1px solid var(--field-line);background:linear-gradient(#fff,#f1f1f1);display:flex;align-items:center;padding-left:9px;font-size:15px}
.select.bold{font-weight:700}
.select .arrow{position:absolute;right:3px;top:3px;width:23px;height:23px;border:1px solid #999;border-radius:2px;background:linear-gradient(#fff,#e3e3e3)}
.option{display:flex;align-items:center;gap:8px;font-size:15px;white-space:nowrap}
.radio{width:18px;height:18px;border:1px solid #aaa;border-radius:50%;background:#fff;position:relative;flex:none}
.checkbox{width:15px;height:15px;border:1px solid #999;background:#fff;position:relative;flex:none}
.radio svg,.checkbox svg{position:absolute;left:1px;top:-2px}
.price{font-weight:700;margin-left:8px}

/* order review */
.review{left:667px;width:305px;font-size:15px}
.review-row{position:absolute;left:0;width:305px;border-bottom:1px solid var(--rule)}
.review-row .p{position:absolute;left:0;line-height:18px}
.review-row .q{position:absolute;left:175px}
.review-row .s{position:absolute;right:0}
.textarea{left:667px;top:658px;width:270px;height:81px;border:1px solid #bdbdbd;background:#fff}
.link{color:var(--maroon);text-decoration:none;border-bottom:1px solid var(--maroon)}

.place-order{left:619px;top:943px;width:353px;height:72px;background:linear-gradient(#f3b54a,#e09a2a);border:2px solid #c9882a;display:flex;align-items:center;padding-left:16px;gap:12px}
.place-order .icon{width:44px;height:44px;border-radius:50%;background:#2e2e2e;border:3px solid #fff;position:relative}
.place-order .text{font-family:"Oswald",sans-serif;font-weight:600;font-size:38px;color:#1e1e1e;letter-spacing:-1px}

/* footer */
.site-footer{left:57px;top:1053px;width:915px;height:119px;background:linear-gradient(#f0f0f0,#f7f7f7)}
.footer-links{display:flex;flex-direction:column;gap:1px}
.footer-links a{font-family:"Oswald",sans-serif;font-weight:500;font-size:13px;line-height:17px;color:#222;text-decoration:none;letter-spacing:-.3px}
.footer-links a.current{color:var(--gold)}
.badge-seal{left:758px;top:1074px;width:62px;height:62px;border-radius:50%;background:#d9b73a;border:4px solid #efd877}
.badge-box{left:833px;top:1072px;width:110px;height:41px;background:#135f8f;border-radius:3px}
.badge-bar{left:836px;top:1120px;width:104px;height:42px;background:#e6eef6;border-radius:3px}
</style>
</head>
<body>
<div class="canvas">
  <div class="frame abs"></div>

  <header class="site-header abs"></header>
  <div class="brand abs"><span class="brand-mark"></span><span class="brand-name">STONELEAF GRANITE</span></div>
  <nav class="main-nav abs">
    <a href="#">HOME</a><a href="#">GALLERY</a><a href="#">QUESTIONS</a><a href="#" class="current">ORDER</a><a href="#">SHOPPING CART</a>
  </nav>

  <h1 class="page-title abs">CHECKOUT</h1>

  <!-- banners -->
  <div class="banner abs" style="left:57px;top:257px">
    <svg width="241" height="58"><defs><linearGradient id="bg1" x1="0" y1="0" x2="0" y2="1"><stop offset="0" stop-color="#4a4540"/><stop offset="1" stop-color="#24211e"/></linearGradient></defs><polygon points="0,0 241,0 241,44 120,57 0,44" fill="url(#bg1)" stroke="#15130f" stroke-width="2"/></svg>
    <span>04.&nbsp; BILLING ADDRESS</span>
  </div>
  <div class="banner abs" style="left:362px;top:257px">
    <svg width="241" height="58"><polygon points="0,0 241,0 241,44 120,57 0,44" fill="url(#bg1)" stroke="#15130f" stroke-width="2"/></svg>
    <span>05. SHIPPING METHOD</span>
  </div>
  <div class="banner abs" style="left:667px;top:257px">
    <svg width="241" height="58"><polygon points="0,0 241,0 241,44 120,57 0,44" fill="url(#bg1)" stroke="#15130f" stroke-width="2"/></svg>
    <span><svg width="28" height="28" style="position:static"><circle cx="14" cy="14" r="12" fill="none" stroke="#fff" stroke-width="2"/><rect x="12.8" y="7" width="2.4" height="9" fill="#fff"/><rect x="12.8" y="18.5" width="2.4" height="2.6" fill="#fff"/></svg>REVIEW YOUR ORDER</span>
  </div>
  <div class="banner abs" style="left:362px;top:542px">
    <svg width="241" height="58"><polygon points="0,0 241,0 241,44 120,57 0,44" fill="url(#bg1)" stroke="#15130f" stroke-width="2"/></svg>
    <span>06. PAYMENT METHOD</span>
  </div>

  <div class="divider abs" style="left:344px"></div>
  <div class="divider abs" style="left:648px"></div>

  <!-- billing address -->
  <section class="billing">
    <div class="label abs" style="left:59px;top:338px">First Name<sup>*</sup></div>
    <div class="field abs" style="left:58px;top:360px;width:270px"></div>
    <div class="label abs" style="left:59px;top:395px">Last Name<sup>*</sup></div>
    <div class="field abs" style="left:58px;top:417px;width:270px"></div>
    <div class="label abs" style="left:59px;top:452px">E-mail Address<sup>*</sup></div>
    <div class="field abs" style="left:58px;top:474px;width:270px"></div>
    <div class="label abs" style="left:59px;top:509px">Telephone<sup>*</sup></div>
    <div class="field abs" style="left:58px;top:531px;width:270px"></div>
    <div class="label abs" style="left:59px;top:566px">Address<sup>*</sup></div>
    <div class="field abs" style="left:58px;top:588px;width:270px"></div>
    <div class="field abs" style="left:58px;top:627px;width:270px"></div>
    <div class="label abs" style="left:59px;top:681px">Country<sup>*</sup></div>
    <div class="field abs" style="left:58px;top:703px;width:270px"></div>
    <div class="label abs" style="left:59px;top:738px">City<sup>*</sup></div>
    <div class="field abs" style="left:58px;top:760px;width:270px"></div>
    <div class="label abs" style="left:59px;top:795px">Zip Code<sup>*</sup></div>
    <div class="label abs" style="left:154px;top:795px">State<sup>*</sup></div>
    <div class="field abs" style="left:58px;top:818px;width:83px"></div>
    <div class="field abs" style="left:153px;top:818px;width:175px"></div>
    <div class="label abs" style="left:59px;top:853px">Fax</div>
    <div class="field abs" style="left:58px;top:875px;width:270px"></div>
    <div class="option abs" style="left:59px;top:934px">
      <span class="checkbox"><svg width="16" height="16"><path d="M2 8 L6 12 L14 2" fill="none" stroke="#333" stroke-width="2"/></svg></span>
      <span style="margin-left:3px">Ship to the same address</span>
    </div>
  </section>

  <!-- shipping method -->
  <section class="shipping">
    <div class="label abs" style="left:362px;top:338px">Warehouse Pickup</div>
    <div class="option abs" style="left:367px;top:362px"><span class="radio"><svg width="18" height="18"><path d="M3 9 L7 13 L15 3" fill="none" stroke="#333" stroke-width="2"/></svg></span><span style="font-weight:700">$ 0.00</span></div>
    <div class="label abs" style="left:362px;top:395px">Garage Delivery within 30 miles</div>
    <div class="option abs" style="left:367px;top:419px"><span class="radio"></span><span>Fixed</span><span class="price">$ 55.00</span></div>
    <div class="label abs" style="left:362px;top:452px">Freght Estimate</div>
    <div class="option abs" style="left:367px;top:476px"><span class="radio"></span><span>Enter Zip Code</span><span class="price">$ 0.00</span></div>
  </section>

  <!-- payment method -->
  <section class="payment">
    <div class="option abs" style="left:367px;top:626px"><span class="radio"></span><span>Write a Check</span></div>
    <div class="option abs" style="left:367px;top:654px"><span class="radio"><svg width="18" height="18"><path d="M3 9 L7 13 L15 3" fill="none" stroke="#333" stroke-width="2"/></svg></span><span>Debit Card Payment</span></div>
    <div class="label abs" style="left:363px;top:681px">Credit Card Type<sup>*</sup></div>
    <div class="select abs" style="left:362px;top:703px;width:270px">-- Please Select --<span class="arrow"><svg width="21" height="21"><path d="M7 6 L10.5 9.5 L14 6 M7 11 L10.5 14.5 L14 11" fill="none" stroke="#333" stroke-width="1.6"/></svg></span></div>
    <div class="label abs" style="left:363px;top:738px">Credit Card Number<sup>*</sup></div>
    <div class="field abs" style="left:362px;top:760px;width:270px;height:31px"></div>
    <div class="label abs" style="left:363px;top:795px">Expiration Date<sup>*</sup></div>
    <div class="select bold abs" style="left:362px;top:818px;width:165px">Month<span class="arrow"><svg width="21" height="21"><path d="M7 6 L10.5 9.5 L14 6 M7 11 L10.5 14.5 L14 11" fill="none" stroke="#333" stroke-width="1.6"/></svg></span></div>
    <div class="select bold abs" style="left:530px;top:818px;width:102px">Year<span class="arrow"><svg width="21" height="21"><path d="M7 6 L10.5 9.5 L14 6 M7 11 L10.5 14.5 L14 11" fill="none" stroke="#333" stroke-width="1.6"/></svg></span></div>
    <div class="label abs" style="left:363px;top:853px">Card Verification Number<sup>*</sup></div>
    <div class="field abs" style="left:362px;top:875px;width:167px;height:31px"></div>
    <a class="link abs" href="#" style="left:538px;top:881px;font-size:12px">What is this?</a>
  </section>

  <!-- review -->
  <section class="review abs" style="top:338px">
    <div class="review-row" style="top:0;height:0;border:none">
      <span class="p">Product</span><span class="q">Qty</span><span class="s">Subtotal</span>
    </div>
    <div class="review-row" style="top:30px;height:60px">
      <span class="p">Imperial White Long<br>Right Corner for<br>Kitchen Countertons</span><span class="q">5</span><span class="s">$129.90</span>
    </div>
    <div class="review-row" style="top:96px;height:41px">
      <span class="p">Imperial White Inside<br>Corner for&nbsp; Kitchen</span><span class="q">5</span><span class="s">$44.95</span>
    </div>
    <div class="review-row" style="top:143px;height:41px">
      <span class="p">Imperial 12x18 Gran-<br>ite Tile</span><span class="q">5</span><span class="s">$18.70</span>
    </div>
    <div class="review-row" style="top:191px;height:24px">
      <span class="s" style="right:95px">Subtotal:</span><span class="s">$193.55</span>
    </div>
    <div class="review-row" style="top:222px;height:24px;font-weight:700;font-size:16px">
      <span class="s" style="right:95px">Grand total:</span><span class="s">$193.55</span>
    </div>
  </section>

  <div class="label abs" style="left:668px;top:635px">Comments</div>
  <div class="textarea abs"><svg class="abs" style="right:2px;bottom:2px" width="10" height="10"><path d="M1 9 L9 1 M5 9 L9 5" stroke="#999"/></svg></div>

  <div class="option abs" style="left:669px;top:763px"><span class="checkbox"><svg width="16" height="16"><path d="M2 8 L6 12 L14 2" fill="none" stroke="#333" stroke-width="2"/></svg></span><span style="margin-left:3px">Subcribe to our newsletter</span></div>
  <div class="option abs" style="left:669px;top:787px;align-items:flex-start"><span class="checkbox" style="margin-top:3px"><svg width="16" height="16"><path d="M2 8 L6 12 L14 2" fill="none" stroke="#333" stroke-width="2"/></svg></span><span style="margin-left:3px;line-height:19px">I have Read and Accept the <a class="link" href="#">Shipping</a><br><a class="link" href="#">Policy</a></span></div>
  <div class="option abs" style="left:669px;top:834px"><span class="checkbox"></span><span style="margin-left:3px">I accept the <a class="link" href="#">Terms and Conditions</a></span></div>

  <a class="place-order abs" href="#" style="text-decoration:none">
    <span class="icon"><svg width="38" height="38" style="position:absolute;left:0;top:0"><path d="M11 19 L17 25 L27 13" fill="none" stroke="#fff" stroke-width="3.5"/></svg></span>
    <span class="text">PLACE ORDER NOW</span>
  </a>

  <!-- footer -->
  <footer class="site-footer abs"></footer>
  <nav class="footer-links abs" style="left:87px;top:1069px">
    <a href="#">HOME</a><a href="#">GALLERY</a><a href="#">QUESTIONS</a><a href="#" class="current">ORDER</a><a href="#">SHOPPING CART</a>
  </nav>
  <nav class="footer-links abs" style="left:290px;top:1069px">
    <a href="#">RETURN POLICY</a><a href="#">SHIPPING POLICY</a><a href="#">PRIVACY</a><a href="#">TERMS OF USE</a><a href="#">CUSTOMER SERVICE</a>
  </nav>
  <nav class="footer-links abs" style="left:515px;top:1069px">
    <a href="#">NEW LINK</a><a href="#">ANOTHER LINK</a><a href="#">THIRD LINK</a><a href="#">FOURTH LINK</a><a href="#">FIFTH LINK</a>
  </nav>
  <div class="badge-seal abs" role="img" aria-label="Payment gateway verification seal"></div>
  <div class="badge-box abs" role="img" aria-label="Business accreditation badge"></div>
  <div class="badge-bar abs" role="img" aria-label="Secure payment provider badge"></div>
</div>
</body>
</html>
```